Building technology company seek stationery design and folder design

Letterhead, and a folder design
ideally, I would have two letter head design, one is for one-page bussiness letter. the other one I can use for longer document such report, or analysis regular report page
you can find company logo and overall style at our website:
www.plinthcove.example

we are in building technology business, using internet of things technology to improve building energy efficiency to make building greener.

Industry/Entity Type

It Company

Requirements
Must have
• company logo
Nice to have
• techy look abstract graphics, etc.
Should not have
• no comment

```html
<!DOCTYPE html>
<html lang="en">
<head>
<meta charset="utf-8">
<title>Plinth Cove Letterhead</title>
<link rel="stylesheet" href="https://fonts.googleapis.com/css2?family=Questrial&family=Roboto:wght@500&display=swap">
<style>
  :root {
    --backdrop: #5d5c68;
    --paper: #ffffff;
    --brand-green: #9dcb3b;
    --brand-green-faint: #f2f7e6;
    --footer-ink: #0b1c1f;
    --footer-text: #ffffff;
  }
  * { margin: 0; padding: 0; box-sizing: border-box; }
  html, body {
    width: 1200px;
    height: 992px;
    overflow: hidden;
    background: var(--backdrop);
  }
  .letterhead {
    position: absolute;
    left: 267px;
    top: 46px;
    width: 666px;
    height: 900px;
    background: var(--paper);
    overflow: hidden;
  }
  .brand {
    position: absolute;
    left: 53px;
    top: 88px;
    display: flex;
    align-items: center;
    gap: 10px;
  }
  .brand-square {
    width: 16px;
    height: 16px;
    background: var(--brand-green);
  }
  .brand-name {
    font-family: "Questrial", sans-serif;
    font-size: 22px;
    letter-spacing: 0.5px;
    color: var(--brand-green);
    text-transform: uppercase;
  }
  .corner-accent {
    position: absolute;
    right: 0;
    bottom: 49px;
    width: 234px;
    height: 168px;
  }
  .contact-band {
    position: absolute;
    left: 0;
    bottom: 9px;
    width: 100%;
    height: 40px;
    background: var(--footer-ink);
    display: flex;
    align-items: center;
    justify-content: center;
    gap: 12px;
    font-family: "Roboto", sans-serif;
    font-weight: 500;
    font-size: 10.5px;
    color: var(--footer-text);
  }
  .contact-item {
    display: flex;
    align-items: center;
    gap: 5px;
  }
  .contact-item svg { width: 9px; height: 9px; }
  .accent-rule {
    position: absolute;
    left: 0;
    bottom: 0;
    width: 100%;
    height: 9px;
    background: var(--brand-green);
  }
</style>
</head>
<body>
  <main class="letterhead">
    <div class="brand">
      <span class="brand-square"></span>
      <span class="brand-name">Plinth Cove</span>
    </div>

    <svg class="corner-accent" viewBox="0 0 234 168" aria-hidden="true">
      <rect x="0" y="0" width="234" height="168" fill="var(--brand-green-faint)"/>
    </svg>

    <footer class="contact-band">
      <span class="contact-item">
        <svg viewBox="0 0 10 10"><path d="M2 0.5 L3.6 2.6 L2.7 3.6 Q3.8 5.9 6.4 7.3 L7.4 6.4 L9.5 8 L8.2 9.5 Q1.5 8 0.5 1.8 Z" fill="var(--brand-green)"/></svg>
        (555) 014-2876
      </span>
      <span class="contact-item">
        <svg viewBox="0 0 10 10"><rect x="0.5" y="2" width="9" height="6.5" fill="var(--brand-green)"/><path d="M0.8 2.3 L5 5.6 L9.2 2.3" stroke="var(--footer-ink)" stroke-width="0.8" fill="none"/></svg>
        info@plinthcove.example
      </span>
      <span class="contact-item">
        <svg viewBox="0 0 10 10"><circle cx="5" cy="5" r="4.3" fill="none" stroke="var(--brand-green)" stroke-width="1"/><ellipse cx="5" cy="5" rx="1.8" ry="4.3" fill="none" stroke="var(--brand-green)" stroke-width="0.8"/><line x1="0.7" y1="5" x2="9.3" y2="5" stroke="var(--brand-green)" stroke-width="0.8"/></svg>
        www.plinthcove.example
      </span>
    </footer>
    <div class="accent-rule"></div>
  </main>
</body>
</html>
```